Home Design company focused on remodel and enhancement of kitchens and bathroorms

I already have a logo designed by ArtHarbor, I now need a design for my business cards.
The company is in the remodeling and enhancement industry for homes, focusing on kitchens and bathrooms, however, we can remodel or enhance every room in a home, an office space, etc.

The company's name is VELMOR HOME DESIGN, LLC

We'll focus on clients in the Rio Grande Valley, Texas. Primarily McAllen, Edinburg, Pharr, Mission, Brownsville and South Padre Island.

The design on the business card should transmit reliability, professionalism anda bit of upscale design.

The logo is in black and white, and would like to keep it that way.

The information that needs to be printed in the business cards is:
Company's name: Velmor Home Design
Company's Logo (attached)
My name: Noel Bramwit
Address, phone and email:
2715 N Parkline Road, Ste 348
Larkmont, TX 79921
(555) 555 0187
nbramwit@velmordesign.example
Website: velmordesign.example

```html
<!DOCTYPE html>
<html lang="en">
<head>
<meta charset="utf-8">
<title>Velmor Home Design – Business Cards</title>
<link rel="stylesheet" href="https://fonts.googleapis.com/css2?family=Lato:wght@400;700&display=swap">
<style>
  :root {
    --backdrop: #d9d9d9;
    --card-black: #1e1c1c;
    --text-white: #f2f2f2;
    --text-faint: #4a4848;
    --silver-dark: #8a8a8a;
    --silver-mid: #c9c9c9;
    --silver-light: #f4f4f4;
    --icon-fill: #1e1c1c;
  }
  * { margin: 0; padding: 0; box-sizing: border-box; }
  html, body { width: 1200px; height: 900px; overflow: hidden; }
  body {
    background: var(--backdrop);
    font-family: "Lato", sans-serif;
    position: relative;
  }
  .card {
    position: absolute;
    top: 150px;
    width: 340px;
    height: 595px;
    background: var(--card-black);
    overflow: hidden;
    box-shadow: 0 10px 28px rgba(0,0,0,0.35);
  }
  .card--front { left: 220px; }
  .card--back { left: 640px; }
  .silver-band {
    position: absolute;
    top: 0;
    width: 52px;
    height: 100%;
    background: linear-gradient(90deg, var(--silver-dark) 0%, var(--silver-light) 35%, var(--silver-mid) 60%, var(--silver-dark) 100%);
  }
  .card--front .silver-band { left: 0; }
  .card--back .silver-band { right: 0; }

  /* front */
  .brand {
    position: absolute;
    top: 52px;
    left: 150px;
    display: flex;
    align-items: stretch;
    gap: 12px;
  }
  .brand__rule { width: 1px; background: var(--text-white); }
  .brand__name {
    color: var(--text-white);
    font-weight: 400;
    font-size: 17px;
    letter-spacing: 4px;
    line-height: 1.05;
  }
  .person-name {
    position: absolute;
    top: 372px;
    left: 86px;
    color: var(--text-white);
    font-weight: 700;
    font-size: 22px;
    letter-spacing: 1.5px;
  }
  .contact-list {
    position: absolute;
    top: 420px;
    left: 38px;
    list-style: none;
  }
  .contact-item {
    display: flex;
    align-items: flex-start;
    gap: 20px;
    color: var(--text-white);
    font-size: 15px;
    line-height: 1.2;
    margin-bottom: 14px;
  }
  .contact-icon { width: 28px; height: 30px; flex: none; margin-top: -4px; }

  /* back */
  .back-wordmark {
    position: absolute;
    top: 60px;
    left: 70px;
    color: var(--text-faint);
    font-weight: 400;
    font-size: 40px;
    letter-spacing: 10px;
    line-height: 1.1;
    writing-mode: vertical-rl;
  }
  .back-rule {
    position: absolute;
    left: 70px;
    top: 300px;
    width: 140px;
    height: 1px;
    background: var(--text-faint);
  }
</style>
</head>
<body>
  <section class="card card--front" aria-label="Business card front">
    <div class="silver-band"></div>
    <div class="brand">
      <div class="brand__rule"></div>
      <div class="brand__name">VELMOR<br>HOME<br>DESIGN</div>
    </div>
    <h1 class="person-name">NOEL BRAMWIT</h1>
    <ul class="contact-list">
      <li class="contact-item">
        <svg class="contact-icon" viewBox="0 0 28 30" aria-hidden="true">
          <polygon points="14,1 27,8 27,22 14,29 1,22 1,8" fill="var(--icon-fill)"/>
          <path d="M9 10 q1-2 3 0 l1 2 q0 1-1 1.5 q1 2.5 3.5 3.5 q.5-1 1.5-1 l2 1 q2 2 0 3 q-3 1-7-3 q-4-4-3-7z" fill="var(--text-white)"/>
        </svg>
        <span>(555) 555 0187</span>
      </li>
      <li class="contact-item">
        <svg class="contact-icon" viewBox="0 0 28 30" aria-hidden="true">
          <polygon points="14,1 27,8 27,22 14,29 1,22 1,8" fill="var(--icon-fill)"/>
          <circle cx="14" cy="15" r="6.5" fill="none" stroke="var(--text-white)" stroke-width="1.4"/>
          <ellipse cx="14" cy="15" rx="2.8" ry="6.5" fill="none" stroke="var(--text-white)" stroke-width="1.2"/>
          <line x1="7.5" y1="15" x2="20.5" y2="15" stroke="var(--text-white)" stroke-width="1.2"/>
        </svg>
        <span>velmordesign.example</span>
      </li>
      <li class="contact-item">
        <svg class="contact-icon" viewBox="0 0 28 30" aria-hidden="true">
          <polygon points="14,1 27,8 27,22 14,29 1,22 1,8" fill="var(--icon-fill)"/>
          <rect x="7.5" y="10.5" width="13" height="9" fill="none" stroke="var(--text-white)" stroke-width="1.4"/>
          <polyline points="7.5,10.5 14,16 20.5,10.5" fill="none" stroke="var(--text-white)" stroke-width="1.4"/>
        </svg>
        <span>nbramwit@velmordesign.example</span>
      </li>
      <li class="contact-item">
        <svg class="contact-icon" viewBox="0 0 28 30" aria-hidden="true">
          <polygon points="14,1 27,8 27,22 14,29 1,22 1,8" fill="var(--icon-fill)"/>
          <path d="M14 22 q-5-6-5-9.5 a5 5 0 0 1 10 0 q0 3.5-5 9.5z" fill="var(--text-white)"/>
          <circle cx="14" cy="12.5" r="2" fill="var(--icon-fill)"/>
        </svg>
        <span>2715 N Parkline Road<br>Ste 348, Larkmont, TX 79921</span>
      </li>
    </ul>
  </section>

  <section class="card card--back" aria-label="Business card back">
    <div class="silver-band"></div>
    <div class="back-wordmark">VELMOR<br>HOME<br>DESIGN</div>
    <div class="back-rule"></div>
  </section>
</body>
</html>
```